New design for www.TrimTable.com

On TrimTable you can find & book your hairdresser. TrimTable is the biggest platform in the Netherlands.

- The design should be a responcive design
- Should be able to go global, should fit in perfectly between all the big booking platforms like roomquay, zipvan etc,
- Should have te result of more bookings. :)
- We are ‘only’ asking a beautiful design, not a technical solution.
- We need a homepage (https://trimtable.com/), search resultpage ((https://trimtable.com/kapper/amsterdam/#), salonpage (https://trimtable.com/kapper/vorden/sol-mira-hair/), about us page (https://trimtable.com/aboutus/), for the hairdresser info page (https://trimtable.com/kapper/), login/register page (https://trimtable.com/account/signin/).

- On the page of the hairdresser there is a dynamic part. The part where you create your appointment. Please take a look at this part too after you choose your treatment (behandeling), employee (medewerker), Date (datum) and time (tijd). The part that you see after this, is the part where you fill in your data as a consumer.

I've added more logo's but mostly we use the green color.

A few of our competitors: www.glowpick.com, www.kestoly.com

Target Market(s)

All consumers

Industry/Entity Type

Hair And Beauty

Number of Pages Required

5+ page

Font styles to use
Sans Serif

Colors
abd036
c3c3c3
757575

Requirements
Must have
• Responsive
• We did an A/B test with the homepage. It turns out that option B works better then option A (take a look at the uploaded pictures). So what we need on the homepage: The USP's with the green checkboxes, The search button needs to by dynamic (changes for example from light green to dark green so you can see you can click it) The call to action sentence Zoek & Vind je kapsalon, the searchfield and searchbutton should be seperated.
Nice to have
• The style that we like is the flat design style. The website should be simple, clean and it should feel a bit like a luxury thing. Because an appointment with the hairdresser can be a real treat and luxury moment for yourself.
• The luxury feeling and flat design that is in the www.zipvan.com website is really nice for example. But then it has to be a bit more light and not so black and dark.

```html
<!DOCTYPE html>
<html lang="nl">
<head>
<meta charset="utf-8">
<title>TrimTable – Zoek &amp; Vind je Kapsalon</title>
<link href="https://fonts.googleapis.com/css2?family=Open+Sans:wght@400;600;700&display=swap" rel="stylesheet">
<style>
:root{
  --green:#abd036;
  --green-dark:#8fb224;
  --grey-light:#c3c3c3;
  --grey:#757575;
  --bg-soft:#ececec;
  --band:#4a4d4f;
  --footer:#3a3c3e;
  --footer-deep:#2e3032;
  --white:#ffffff;
  --ink:#3b3b3b;
}
*{box-sizing:border-box;margin:0;padding:0}
html,body{width:887px;height:1200px;overflow:hidden;font-family:"Open Sans",Arial,sans-serif;color:var(--ink);background:var(--white)}
.page{width:887px;height:1200px;position:relative}

/* hero */
.hero{position:relative;height:527px;overflow:hidden}
.hero-photo{position:absolute;inset:0;background:radial-gradient(ellipse at 50% 45%,#6b6d6b 0%,#454746 45%,#232423 100%)}
.hero-shade{position:absolute;inset:0;background:rgba(20,20,20,.25)}
.topnav{position:absolute;top:30px;right:46px;display:flex;gap:8px}
.topnav a{font-size:10px;color:var(--white);text-decoration:none;padding:6px 10px;letter-spacing:.5px}
.topnav .login{border:1px solid var(--white)}
.brand{position:absolute;top:72px;left:0;right:0;display:flex;justify-content:center;align-items:center;gap:10px}
.brand-dot{width:30px;height:30px;border-radius:50%;background:var(--green)}
.brand-name{font-size:36px;font-weight:700;color:var(--green)}
.tagline{position:absolute;top:160px;left:0;right:0;text-align:center;color:var(--white);font-size:22px;font-weight:700}
.search{position:absolute;top:222px;left:296px;display:flex;gap:10px}
.search-field{width:206px;height:32px;background:var(--white);border:0;font-size:10px;color:var(--grey);padding:0 10px;display:flex;align-items:center}
.search-btn{width:80px;height:32px;background:var(--green);color:var(--white);font-size:11px;font-weight:600;display:flex;align-items:center;justify-content:center;transition:background .2s}
.search-btn:hover{background:var(--green-dark)}
.usps{position:absolute;top:451px;left:0;right:0;display:flex;justify-content:center;gap:44px;color:var(--white);font-size:11px}
.usp{display:flex;align-items:center;gap:7px}

/* testimonials */
.reviews{height:311px;background:var(--bg-soft);display:flex;justify-content:center;gap:34px;padding-top:34px}
.card{width:194px;height:238px;background:var(--white);position:relative;text-align:center;padding:46px 18px 0}
.card-icon{position:absolute;top:-16px;left:50%;margin-left:-17px;width:34px;height:34px;border-radius:50%;background:var(--green);display:flex;align-items:center;justify-content:center}
.card h3{font-size:14px;font-weight:700;margin-bottom:14px;color:var(--ink)}
.card p{font-size:9.5px;line-height:1.6;color:var(--grey);font-style:italic}
.card .who{margin-top:14px;font-size:9px;color:var(--green);font-style:normal}

/* subscribe */
.subscribe{height:56px;background:var(--band);display:flex;align-items:center;justify-content:center;gap:12px;color:var(--white);font-size:11px;font-weight:600}
.subscribe-field{width:140px;height:26px;background:var(--white);font-size:9px;font-weight:400;color:var(--grey);display:flex;align-items:center;padding:0 8px}
.subscribe-btn{width:26px;height:26px;background:var(--green);display:flex;align-items:center;justify-content:center}

/* footer */
.footer{background:var(--footer);height:306px;color:#cfcfcf;padding:28px 54px 0;position:relative}
.footer-cols{display:flex;justify-content:space-between}
.footer-col{width:230px}
.footer h4{font-size:11px;font-weight:700;color:var(--white);margin-bottom:8px}
.footer li{list-style:none;font-size:9px;line-height:1.7}
.social{display:flex;gap:6px}
.social span{width:18px;height:18px;border-radius:50%;background:#9a9c9e}
.footer hr{border:0;border-top:1px solid #515456;margin:16px 0 12px}
.footer .intro{font-size:9px;line-height:1.6;margin-top:4px}
.cities{display:flex;justify-content:space-between;margin-top:14px}
.cities ul{width:230px}
.copyright{position:absolute;left:0;right:0;bottom:0;height:26px;background:var(--footer-deep);font-size:8.5px;color:#9a9a9a;display:flex;align-items:center;justify-content:center}
</style>
</head>
<body>
<div class="page">

  <header class="hero">
    <div class="hero-photo" role="img" aria-label="Photo of a barber trimming a client's hair in a classic barbershop"></div>
    <div class="hero-shade"></div>
    <nav class="topnav">
      <a href="#">REGISTREER</a>
      <a href="#" class="login">LOGIN</a>
    </nav>
    <div class="brand"><span class="brand-dot"></span><span class="brand-name">TrimTable</span></div>
    <h1 class="tagline">Zoek &amp; Vind je Kapsalon</h1>
    <div class="search">
      <div class="search-field">Stad en Plaats of Postcode</div>
      <div class="search-btn">Zoek kapper</div>
    </div>
    <ul class="usps">
      <li class="usp"><svg width="14" height="14" viewBox="0 0 14 14"><circle cx="7" cy="7" r="7" fill="#abd036"/><path d="M4 7.2l2 2 4-4.4" stroke="#fff" stroke-width="1.6" fill="none"/></svg>Grootste kappersboekingsite van NL</li>
      <li class="usp"><svg width="14" height="14" viewBox="0 0 14 14"><circle cx="7" cy="7" r="7" fill="#abd036"/><path d="M4 7.2l2 2 4-4.4" stroke="#fff" stroke-width="1.6" fill="none"/></svg>Afspraak met 100% zekerheid</li>
      <li class="usp"><svg width="14" height="14" viewBox="0 0 14 14"><circle cx="7" cy="7" r="7" fill="#abd036"/><path d="M4 7.2l2 2 4-4.4" stroke="#fff" stroke-width="1.6" fill="none"/></svg>Meer dan 10.000 kapper reviews</li>
    </ul>
  </header>

  <section class="reviews">
    <article class="card">
      <div class="card-icon"><svg width="14" height="14" viewBox="0 0 14 14"><path d="M3 7.3l2.6 2.6L11 4.3" stroke="#fff" stroke-width="2" fill="none"/></svg></div>
      <h3>Fantastisch!</h3>
      <p>"Eindelijk een afspraak maken zonder te bellen. Snel gevonden en direct geboekt, en mijn kapper was erg vriendelijk."</p>
      <p class="who">Tim, Amsterdam</p>
    </article>
    <article class="card">
      <div class="card-icon"><svg width="14" height="14" viewBox="0 0 14 14"><path d="M3 7.3l2.6 2.6L11 4.3" stroke="#fff" stroke-width="2" fill="none"/></svg></div>
      <h3>Superfijn!</h3>
      <p>"Superfijn geboekt en binnen een dag had ik een nieuwe kapper!"</p>
      <p class="who">Sanne, Utrecht</p>
    </article>
    <article class="card">
      <div class="card-icon"><svg width="14" height="14" viewBox="0 0 14 14"><path d="M3 7.3l2.6 2.6L11 4.3" stroke="#fff" stroke-width="2" fill="none"/></svg></div>
      <h3>Handige Recensies</h3>
      <p>"Dankzij de echte recensies op de website kon ik via TrimTable eenvoudig mijn nieuwe vaste kapper kiezen en boeken."</p>
      <p class="who">Joris, Rotterdam</p>
    </article>
  </section>

  <section class="subscribe">
    <span>How TrimTable get tips? Subscribe</span>
    <div class="subscribe-field">Wat is je emailadres?</div>
    <div class="subscribe-btn"><svg width="10" height="10" viewBox="0 0 10 10"><path d="M2 5h6M5.5 2.5L8 5 5.5 7.5" stroke="#fff" stroke-width="1.5" fill="none"/></svg></div>
  </section>

  <footer class="footer">
    <div class="footer-cols">
      <div class="footer-col">
        <h4>TrimTable</h4>
        <ul><li>About Us</li><li>Werk at Blog</li></ul>
      </div>
      <div class="footer-col">
        <h4>Follow Us</h4>
        <div class="social"><span></span><span></span><span></span></div>
      </div>
      <div class="footer-col">
        <h4>For The Entrepreneur</h4>
        <ul><li>I have a salon and want to register</li><li>TrimTable Login here</li></ul>
      </div>
    </div>
    <hr>
    <h4>Make an appointment at the hairdresser in one of these places:</h4>
    <p class="intro">Choose a hairdresser and make your appointment directly. Online booking is simple in every city of the Netherlands. Find a hairdresser in Amsterdam, a hairdresser in Utrecht, a hairdresser in Groningen or a hairdresser in Maastricht. What are you waiting for?</p>
    <div class="cities">
      <ul><li>Barber Amsterdam</li><li>Barber Rotterdam</li><li>Barber Nijmegen</li></ul>
      <ul><li>Barber Almere</li><li>Barber Groningen</li><li>Barber Arnhem</li></ul>
      <ul><li>Barber Breda</li><li>Barber Eindhoven</li><li>Barber Haarlem</li></ul>
    </div>
    <div class="copyright">Copyright © 2015 TrimTable. All Rights Reserved.</div>
  </footer>

</div>
</body>
</html>
```